TalkBridge - Language Coaching Services

Sleek, innovative, trendy design for Language Coaching business.

TalkBridge is a new UK based company that provides Language Coaching services. We offer highly personalized on-line and face to face language courses. We also impart learning techniques workshops based on the latest neuroscience research for second-language acquisition.

Target Market(s)

Industry/Entity Type

Consulting

Contact Information for Business Card

TalkBridge
ElenaVT@talkbridge-demo.co.uk
TalkBridge-demo.co.uk
London, UK

Font styles to use
Sans Serif

```html
<!DOCTYPE html>
<html lang="en">
<head>
<meta charset="utf-8">
<title>TalkBridge Business Card</title>
<link rel="stylesheet" href="https://fonts.googleapis.com/css2?family=Montserrat:wght@400;500;700;800&display=swap">
<style>
  :root {
    --bg: #3c3c3b;
    --blue-deep: #0b5c8f;
    --blue-mid: #0e78b4;
    --blue-light: #1ba6dd;
    --brand: #1593cf;
    --ink: #2f2f2f;
    --rule: #8a8a8a;
    --white: #ffffff;
  }
  * { box-sizing: border-box; margin: 0; padding: 0; }
  html, body { width: 1200px; height: 895px; overflow: hidden; }
  body {
    background: var(--bg);
    font-family: "Montserrat", sans-serif;
    position: relative;
  }
  .card {
    position: absolute;
    width: 540px;
    height: 309px;
    border-radius: 22px;
    overflow: hidden;
  }
  .card-front {
    left: 70px; top: 80px;
    background: radial-gradient(ellipse at 50% 38%, var(--blue-light) 0%, var(--blue-mid) 45%, var(--blue-deep) 100%);
    color: var(--white);
  }
  .card-back {
    left: 590px; top: 505px;
    background: var(--white);
    color: var(--ink);
  }
  .brand {
    display: flex;
    align-items: center;
    gap: 12px;
  }
  .brand-dot {
    width: 34px; height: 34px;
    border-radius: 50%;
    border: 5px solid currentColor;
  }
  .brand-name {
    font-weight: 700;
    font-size: 36px;
    letter-spacing: 1px;
  }
  .card-front .brand {
    position: absolute;
    left: 0; right: 0; top: 92px;
    justify-content: center;
  }
  .services {
    position: absolute;
    bottom: 28px;
    list-style: none;
    font-size: 11px;
    font-weight: 500;
    line-height: 1.55;
  }
  .services li::before {
    content: "";
    display: inline-block;
    width: 4px; height: 4px;
    border-radius: 50%;
    background: var(--white);
    margin-right: 8px;
    vertical-align: middle;
  }
  .services-left { left: 30px; }
  .services-right { left: 290px; }
  .card-back .brand {
    position: absolute;
    left: 34px; top: 134px;
    color: var(--brand);
  }
  .card-back .brand-name { font-size: 28px; }
  .card-back .brand-dot { width: 30px; height: 30px; border-width: 4px; }
  .divider {
    position: absolute;
    left: 300px; top: 60px;
    width: 1px; height: 190px;
    background: var(--rule);
  }
  .contact {
    position: absolute;
    left: 322px; top: 62px;
  }
  .person-name {
    font-size: 20px;
    color: var(--brand);
    font-weight: 400;
  }
  .person-name strong { font-weight: 800; }
  .role { font-size: 12px; margin-top: 2px; }
  .city { font-size: 12px; margin-top: 18px; }
  .details { list-style: none; margin-top: 14px; font-size: 11.5px; line-height: 1.9; }
  .details li { display: flex; align-items: center; gap: 7px; }
  .details svg { width: 11px; height: 11px; fill: var(--brand); flex: none; }
</style>
</head>
<body>
  <section class="card card-front">
    <div class="brand">
      <span class="brand-dot"></span>
      <span class="brand-name">TALKBRIDGE</span>
    </div>
    <ul class="services services-left">
      <li>Face to face language coaching session</li>
      <li>On-line language coaching session</li>
      <li>Personalized Newsletters for self-learners</li>
    </ul>
    <ul class="services services-right">
      <li>Language Learning Techniques Workshops</li>
      <li>Mindful Learning Workshops</li>
      <li>Access to premium content, resources</li>
    </ul>
  </section>

  <section class="card card-back">
    <div class="brand">
      <span class="brand-dot"></span>
      <span class="brand-name">TALKBRIDGE</span>
    </div>
    <div class="divider"></div>
    <div class="contact">
      <p class="person-name"><strong>ELENA</strong> VT</p>
      <p class="role">Director</p>
      <p class="city">London, UK</p>
      <ul class="details">
        <li><svg viewBox="0 0 16 16"><path d="M3 1l3 3-2 2c1 2 3 4 5 5l2-2 3 3-2 3C6 14 2 10 1 4z"/></svg>020 7946 0321</li>
        <li><svg viewBox="0 0 16 16"><path d="M1 3h14v10H1z M1 3l7 6 7-6" stroke="#fff" stroke-width="1"/></svg>ElenaVT@talkbridge-demo.co.uk</li>
        <li><svg viewBox="0 0 16 16"><circle cx="8" cy="8" r="7"/><path d="M1 8h14M8 1v14" stroke="#fff" stroke-width="1"/></svg>www.talkbridge-demo.co.uk</li>
      </ul>
    </div>
  </section>
</body>
</html>
```